Urgent - brand new business card for a startup technical advisory and incubation business in Sydney

We need a brand new business card design for BrightForge. We are a startup technical advisory and incubation business based in Sydney Australia. We work with entrepreneurs and innovators to help rapidly and efficiently turn their ideas into reality and to ensure they have the technical platform required for growth.

Our name is partly inspired by our love of lean product development methods and the lean startup movement.

We would like clean, uncluttered designs that feature our two logo colours and communicate a professional but creative, in-touch and entrepreneurial business.

PLEASE SEE MUST HAVE PRIORITIES FOR DRAFT CONTACT INFORMATION AND OTHER DESIRED TEXT ON CARD.
Updates

We have now updated the brief to include draft business card contact information and also some additional desired text to feature on the card design.    Please review the Must Have priorities.

Also final updated source files for the horizontal and vertical versions have now been uploaded and should be used for any designs.

Thanks!

Target Market(s)

Entrepeneurs, innovators, startup investors looking for a strong product development partner

Industry/Entity Type

Business

Requirements
Must have
• Feature our two logo colours
Be a relatively clean, pared back overall design - quite minimalist

Updated source files (AI) for vertical and horizontal layouts attached.

Draft contact information for business card:
Neil Barton
Founder & CTO
Phone: +61 427 555123
Email: xxxx@brightforge.com
Voicelink: xxxxxbarton
Chirper: nbarton

www.brightforge.com

We would also like the overall design to include the phrase "You have great ideas. Let us make them happen." (probably in a reasonably subtle way)

Nice to have
• Inspire me! Double-sided designs are fine with logo, phrase, (URL?) on one side and contact details on other (+ any other design elements)

Logo on business card can be either with lightbulb above the wording as per example here or to the left of the BrightForge wording - both layouts in files provided.
Should not have
• Shouldn't look like a Pentara Suite business card template :-)

```html
<!DOCTYPE html>
<html lang="en">
<head>
<meta charset="utf-8">
<title>BrightForge — Business Card Set</title>
<link rel="stylesheet" href="https://fonts.googleapis.com/css2?family=PT+Sans:wght@400;700&display=swap">
<style>
  :root {
    --brand-cyan: #00b6ef;
    --brand-ink: #1f2b31;
    --card-dark: #16232a;
    --card-white: #ffffff;
    --text-main: #2b2b2b;
    --grid-light: rgba(0, 0, 0, 0.06);
    --grid-dark: rgba(0, 182, 239, 0.12);
    --backdrop: #3b2418;
  }
  * { margin: 0; padding: 0; box-sizing: border-box; }
  html, body {
    width: 1200px;
    height: 836px;
    overflow: hidden;
    background: var(--backdrop);
    font-family: "PT Sans", sans-serif;
  }
  .sheet { position: relative; width: 1200px; height: 836px; }

  .card {
    position: absolute;
    width: 464px;
    height: 264px;
    overflow: hidden;
    box-shadow: 0 3px 8px rgba(0, 0, 0, 0.45);
  }
  .card--contact {
    left: 118px; top: 118px;
    background-color: var(--card-white);
    background-image:
      linear-gradient(var(--grid-light) 1px, transparent 1px),
      linear-gradient(90deg, var(--grid-light) 1px, transparent 1px);
    background-size: 10px 10px;
  }
  .card--dark {
    left: 611px; top: 118px;
    background-color: var(--card-dark);
    background-image:
      linear-gradient(var(--grid-dark) 1px, transparent 1px),
      linear-gradient(90deg, var(--grid-dark) 1px, transparent 1px);
    background-size: 10px 10px;
  }
  .card--white { left: 120px; top: 430px; background: var(--card-white); }
  .card--cyan { left: 612px; top: 430px; background: var(--brand-cyan); }

  /* contact side */
  .holder {
    position: absolute; left: 30px; top: 24px;
    color: var(--text-main);
    font-size: 22px;
  }
  .holder__role { font-size: 11px; margin-left: 2px; }
  .contact-list { position: absolute; left: 30px; top: 96px; list-style: none; }
  .contact-list li {
    display: flex; align-items: center; gap: 6px;
    font-size: 12px; color: var(--text-main);
    height: 20px;
  }
  .contact-list svg { width: 12px; height: 12px; }
  .social-tabs { position: absolute; left: 0; top: 167px; list-style: none; }
  .social-tabs li {
    width: 151px; height: 22px; margin-bottom: 4px;
    background: var(--brand-cyan);
    border-radius: 0 11px 11px 0;
    color: #fff; font-size: 11.5px;
    line-height: 22px; padding-left: 30px;
  }
  .brand-mark {
    position: absolute; left: 302px; top: 92px;
    width: 70px; height: 70px; border-radius: 50%;
    background: var(--brand-cyan);
  }
  .brand-name {
    position: absolute; right: 38px; top: 192px;
    font-weight: 700; font-size: 30px;
    color: var(--brand-ink);
    letter-spacing: -0.5px;
  }

  /* brand sides */
  .brand-block {
    position: absolute; left: 0; width: 100%;
    display: flex; flex-direction: column; align-items: center; gap: 10px;
  }
  .brand-block__circle { width: 82px; height: 82px; border-radius: 50%; }
  .brand-block__name { font-weight: 700; font-size: 22px; }
  .card--dark .brand-block { top: 40px; }
  .card--dark .brand-block__circle { background: #fff; }
  .card--dark .brand-block__name { color: #fff; }
  .card--white .brand-block { top: 58px; }
  .card--white .brand-block__circle { background: var(--brand-cyan); }
  .card--white .brand-block__name { color: var(--brand-ink); }
  .card--cyan .brand-block { top: 58px; }
  .card--cyan .brand-block__circle { background: #fff; }
  .card--cyan .brand-block__name { color: #fff; }

  .tagline-band {
    position: absolute; left: 0; top: 200px;
    width: 100%; height: 39px;
    background: var(--brand-cyan);
    color: #fff; font-size: 15px; text-transform: uppercase;
    display: flex; align-items: center; justify-content: center;
    letter-spacing: 0.2px;
  }
  .tagline {
    position: absolute; left: 0; width: 100%;
    text-align: center; font-size: 15px;
  }
  .card--white .tagline { top: 222px; color: var(--text-main); }
  .card--cyan .tagline { top: 228px; color: #fff; text-transform: uppercase; }
</style>
</head>
<body>
<main class="sheet">

  <section class="card card--contact" aria-label="Contact side">
    <h1 class="holder"><span style="font-weight:400">Neil Barton,</span> <span class="holder__role">Founder &amp; CTO</span></h1>
    <ul class="contact-list">
      <li>
        <svg viewBox="0 0 12 12" aria-hidden="true"><circle cx="6" cy="6" r="6" fill="var(--brand-cyan)"/><path d="M4 3l1.3 1.4-.6.9c.4.9 1 1.5 1.9 1.9l.9-.6L9 8l-.7 1C6 9 3 6 3 3.7z" fill="#fff"/></svg>
        +61 427 555123
      </li>
      <li>
        <svg viewBox="0 0 12 12" aria-hidden="true"><rect x="0" y="2" width="12" height="8" rx="1.5" fill="var(--brand-cyan)"/><path d="M1 3l5 3.5L11 3" stroke="#fff" stroke-width="1" fill="none"/></svg>
        xxxx@brightforge.com
      </li>
    </ul>
    <ul class="social-tabs">
      <li>Voicelink: xxxxxbarton</li>
      <li>Chirper: nbarton</li>
      <li>www.brightforge.com</li>
    </ul>
    <div class="brand-mark" aria-hidden="true"></div>
    <div class="brand-name">BrightForge</div>
  </section>

  <section class="card card--dark" aria-label="Brand side, dark">
    <div class="brand-block">
      <div class="brand-block__circle" aria-hidden="true"></div>
      <div class="brand-block__name">BrightForge</div>
    </div>
    <p class="tagline-band">You have great ideas.&nbsp; Let us make them happen.</p>
  </section>

  <section class="card card--white" aria-label="Brand side, white">
    <div class="brand-block">
      <div class="brand-block__circle" aria-hidden="true"></div>
      <div class="brand-block__name">BrightForge</div>
    </div>
    <p class="tagline">You have great ideas.&nbsp; Let us make them happen.</p>
  </section>

  <section class="card card--cyan" aria-label="Brand side, cyan">
    <div class="brand-block">
      <div class="brand-block__circle" aria-hidden="true"></div>
      <div class="brand-block__name">BrightForge</div>
    </div>
    <p class="tagline">You have great ideas.&nbsp; Let us make them happen.</p>
  </section>

</main>
</body>
</html>
```